Basic business card

use my newly created logo - and the phrases (Leaner Silicon Testing & Faster Product Launch Readiness) - and my new email domain / ID - use at conferences / tradeshows

Industry/Entity Type

semiconductor

Contact Information for Business Card

Lewis K Hardy, Owner, communicate via Logo - Lower COT - Cost of Test, Accelerated NPI - New Product Introduction, phone +1 480 555 0162, Brennick Falls, Oravale, USA, lewis.hardy@vexalon-tsq.com

Font styles to use
Sans Serif

Requirements
Nice to have
• re-use my logo created via Artisan Hive last August (#5918206)

```html
<!DOCTYPE html>
<html lang="en">
<head>
<meta charset="utf-8">
<title>Vexalon-TSQ Business Card</title>
<link rel="stylesheet" href="https://fonts.googleapis.com/css2?family=Montserrat:wght@300;400;500;700&display=swap">
<style>
  :root {
    --page-bg: #24272d;
    --card-bg: #4a5874;
    --card-pattern-a: #45536e;
    --card-pattern-b: #51607c;
    --edge-cyan: #3ec4e8;
    --name-green: #7cc242;
    --text-white: #ffffff;
    --icon-cyan: #3ec4e8;
  }
  * { box-sizing: border-box; margin: 0; padding: 0; }
  html, body {
    width: 1200px; height: 900px; overflow: hidden;
    background: var(--page-bg);
    font-family: "Montserrat", sans-serif;
    color: var(--text-white);
  }
  .stage {
    width: 1200px; height: 900px;
    display: flex; flex-direction: column; align-items: center; justify-content: center;
    gap: 44px;
  }
  .card {
    position: relative;
    width: 620px; height: 354px;
    border-radius: 22px;
    background: var(--card-bg);
    border-bottom: 4px solid var(--edge-cyan);
    border-right: 2px solid var(--edge-cyan);
    overflow: hidden;
  }
  /* Front */
  .identity { position: absolute; left: 44px; top: 62px; }
  .identity__name {
    font-weight: 700; font-size: 30px; color: var(--name-green); letter-spacing: 0.5px;
  }
  .identity__role { font-weight: 300; font-size: 17px; margin-top: 2px; }
  .divider {
    position: absolute; left: 44px; top: 148px; width: 500px; height: 1.5px;
    background: linear-gradient(90deg, var(--name-green), rgba(124,194,66,0));
  }
  .contacts { position: absolute; left: 44px; top: 172px; list-style: none; }
  .contacts li {
    display: flex; align-items: center; gap: 10px;
    font-size: 16px; font-weight: 400; line-height: 30px;
  }
  .contacts svg { width: 15px; height: 15px; fill: var(--icon-cyan); flex: none; }
  .brand { display: flex; align-items: center; gap: 10px; }
  .brand__dot { width: 14px; height: 14px; background: var(--text-white); flex: none; }
  .brand__name { font-weight: 500; font-size: 28px; letter-spacing: 1px; color: var(--text-white); white-space: nowrap; }
  .card--front .brand { position: absolute; right: 40px; top: 192px; }
  /* Back */
  .card__pattern {
    position: absolute; inset: 0;
    background: linear-gradient(135deg, var(--card-pattern-a), var(--card-pattern-b) 50%, var(--card-pattern-a));
  }
  .card--back .lockup {
    position: absolute; inset: 0;
    display: flex; flex-direction: column; align-items: center; justify-content: center; gap: 18px;
  }
  .card--back .brand__name { font-size: 40px; }
  .tagline { font-size: 15px; font-weight: 400; letter-spacing: 0.5px; white-space: nowrap; }
</style>
</head>
<body>
<main class="stage">
  <section class="card card--front">
    <div class="identity">
      <h1 class="identity__name">Lewis K Hardy</h1>
      <p class="identity__role">Owner</p>
    </div>
    <div class="divider"></div>
    <ul class="contacts">
      <li>
        <svg viewBox="0 0 24 24" aria-hidden="true"><path d="M6.6 10.8a15 15 0 0 0 6.6 6.6l2.2-2.2a1 1 0 0 1 1-.25 11.4 11.4 0 0 0 3.6.57 1 1 0 0 1 1 1V20a1 1 0 0 1-1 1A17 17 0 0 1 3 4a1 1 0 0 1 1-1h3.5a1 1 0 0 1 1 1c0 1.25.2 2.45.57 3.57a1 1 0 0 1-.25 1z"/></svg>
        +1 480 555 0162
      </li>
      <li>
        <svg viewBox="0 0 24 24" aria-hidden="true"><path d="M2 5h20v14H2zm2 2v.5l8 5 8-5V7zm0 2.9V17h16V9.9l-8 5z"/></svg>
        lewis.hardy@vexalon-tsq.com
      </li>
      <li>
        <svg viewBox="0 0 24 24" aria-hidden="true"><path d="M12 2a7 7 0 0 0-7 7c0 5.2 7 13 7 13s7-7.8 7-13a7 7 0 0 0-7-7zm0 9.5A2.5 2.5 0 1 1 12 6.5a2.5 2.5 0 0 1 0 5z"/></svg>
        Brennick Falls, Oravale, USA
      </li>
    </ul>
    <div class="brand">
      <span class="brand__dot"></span>
      <span class="brand__name">VEXALON-TSQ</span>
    </div>
  </section>

  <section class="card card--back">
    <div class="card__pattern" role="img" aria-label="Faint repeating brand-mark pattern across the card background"></div>
    <div class="lockup">
      <div class="brand">
        <span class="brand__dot"></span>
        <span class="brand__name">VEXALON-TSQ</span>
      </div>
      <p class="tagline">Leaner Silicon Testing &amp; Faster Product Launch Readiness</p>
    </div>
  </section>
</main>
</body>
</html>
```